Process Roadmap for Interior Design Firm

We are looking to ramp up the design appeal of our current process roadmap to be very visually interesting, while staying informative and descriptive about our process.

Target Market(s)

In-house Clients

Industry/Entity Type

Interior Design Firm focused on sustainable and holistic design.

Other font styles liked:
• raleway

Requirements
Must have
• 1.) it would be nice if the graphic provided a more clear indication of the “journey” from one step to the next, so that there was a clear sense of the progression (such that we are directing the viewer) 2.). We would want it to fit on an 8.5”x11” page (the page could be horizontal when we have the Steady Pathway formatted out with the testimonials) (in addition to the testimonials, we may also want to have the detailed descriptions of each step of the process presented below the graphic, so that the graphic is cleaner) 3.) ideally the graphic is clear and simple enough to also be used on our Bi-Weekly Client Updates, which will be typed updates for clients re their project budgets, schedule and scope. The Steady Pathway graphic (without all the testimonials) would be at the end of the update, and would fit on the page horizontally at the bottom, perhaps in a space which is 7.5”w x 4”h or so.
Should not have
• bold or bright colors. Natural neutrals are preferred, such as the ones featured on the provided graphic.

```html
<!DOCTYPE html>
<html lang="en">
<head>
<meta charset="utf-8">
<title>KLR Steady Pathway</title>
<link href="https://fonts.googleapis.com/css2?family=Oswald:wght@400;500&family=Open+Sans:wdth,wght@75..100,500..700&display=swap" rel="stylesheet">
<style>
  :root {
    --page: #ffffff;
    --sand: #e9e3d8;
    --ray: rgba(255, 253, 248, 0.55);
    --sage: #7f8c6e;
    --sage-deep: #5f6b52;
    --taupe: #6e6558;
    --stone-light: #b3a897;
    --stone-dark: #6f6556;
    --white: #ffffff;
  }
  html, body {
    margin: 0;
    padding: 0;
    width: 848px;
    height: 1200px;
    overflow: hidden;
    background: var(--page);
  }
  .page {
    position: relative;
    width: 848px;
    height: 1200px;
    background: var(--page);
  }
  .roadmap {
    position: absolute;
    left: 0;
    top: 0;
    width: 848px;
    height: 1200px;
    display: block;
  }
  .step-label {
    font-family: "Oswald", sans-serif;
    font-weight: 500;
    font-size: 11.5px;
    fill: var(--sage-deep);
    text-anchor: middle;
  }
  .step-number {
    font-family: "Open Sans", sans-serif;
    font-weight: 700;
    font-size: 10.5px;
    fill: var(--sage-deep);
    text-anchor: middle;
  }
  .pathway-title {
    font-family: "Open Sans", sans-serif;
    font-stretch: 80%;
    font-weight: 600;
    font-size: 23px;
    fill: var(--white);
    letter-spacing: 0.4px;
  }
  .sand { fill: var(--sand); }
  .ray { fill: var(--ray); }
  .arc-band { fill: none; stroke: var(--white); stroke-width: 7; }
  .leader { stroke: var(--white); stroke-width: 0.9; }
  .step-dot { fill: var(--white); }
  .journey-arrow { fill: var(--sage); }
  .icon-face { fill: var(--sage); }
  .icon-side { fill: var(--sage-deep); }
  .icon-glyph { fill: none; stroke: var(--white); stroke-width: 1.4; stroke-linecap: round; stroke-linejoin: round; }
  .icon-solid { fill: var(--white); }
</style>
</head>
<body>
<main class="page">
  <svg class="roadmap" viewBox="0 0 595 842" xmlns="http://www.w3.org/2000/svg">
    <defs>
      <linearGradient id="roomTone" x1="0" y1="0" x2="1" y2="1">
        <stop offset="0" stop-color="var(--stone-light)"/>
        <stop offset="1" stop-color="var(--stone-dark)"/>
      </linearGradient>
      <path id="titleCurve" d="M 160 786 C 225 752, 370 752, 440 786"/>
    </defs>

    <rect class="sand" x="0" y="628" width="595" height="214"/>

    <g class="rays">
      <polygon class="ray" points="495,765 300,628 360,628"/>
      <polygon class="ray" points="495,765 430,628 470,628"/>
      <polygon class="ray" points="495,765 520,628 565,628"/>
      <polygon class="ray" points="495,765 595,650 595,690"/>
      <polygon class="ray" points="495,765 595,735 595,760"/>
      <polygon class="ray" points="495,765 595,800 595,830"/>
    </g>

    <path d="M48 842 C55 800, 75 775, 102 764 C160 740, 230 731, 297 731 C364 731, 434 740, 492 764 C519 775, 539 800, 548 842 Z"
          fill="url(#roomTone)" role="img" aria-label="Photo of a bright furnished living room with shuttered windows"/>

    <path class="arc-band" d="M48 842 C55 800, 75 775, 102 764 C160 740, 230 731, 297 731 C364 731, 434 740, 492 764 C519 775, 539 800, 548 842"/>

    <text class="pathway-title"><textPath href="#titleCurve" startOffset="50%" text-anchor="middle">KLR STEADY PATHWAY</textPath></text>

    <g>
      <line class="leader" x1="102" y1="735" x2="102" y2="764"/>
      <line class="leader" x1="166" y1="713" x2="166" y2="744"/>
      <line class="leader" x1="231" y1="700" x2="231" y2="734"/>
      <line class="leader" x1="296" y1="700" x2="296" y2="731"/>
      <line class="leader" x1="362" y1="700" x2="362" y2="734"/>
      <line class="leader" x1="428" y1="713" x2="428" y2="744"/>
      <line class="leader" x1="492" y1="735" x2="492" y2="764"/>
    </g>

    <!-- journey arrows between steps, pointing forward along the path -->
    <g>
      <path class="journey-arrow" d="M-3 -2.5 L3 0 L-3 2.5 Z" transform="translate(134,753) rotate(-21)"/>
      <path class="journey-arrow" d="M-3 -2.5 L3 0 L-3 2.5 Z" transform="translate(198,739) rotate(-9)"/>
      <path class="journey-arrow" d="M-3 -2.5 L3 0 L-3 2.5 Z" transform="translate(263,732) rotate(-3)"/>
      <path class="journey-arrow" d="M-3 -2.5 L3 0 L-3 2.5 Z" transform="translate(329,732) rotate(3)"/>
      <path class="journey-arrow" d="M-3 -2.5 L3 0 L-3 2.5 Z" transform="translate(395,739) rotate(9)"/>
      <path class="journey-arrow" d="M-3 -2.5 L3 0 L-3 2.5 Z" transform="translate(460,753) rotate(21)"/>
    </g>

    <g>
      <circle class="step-dot" cx="102" cy="764" r="9.5"/><text class="step-number" x="102" y="768">1</text>
      <circle class="step-dot" cx="166" cy="744" r="9.5"/><text class="step-number" x="166" y="748">2</text>
      <circle class="step-dot" cx="231" cy="734" r="9.5"/><text class="step-number" x="231" y="738">3</text>
      <circle class="step-dot" cx="296" cy="731" r="9.5"/><text class="step-number" x="296" y="735">4</text>
      <circle class="step-dot" cx="362" cy="734" r="9.5"/><text class="step-number" x="362" y="738">5</text>
      <circle class="step-dot" cx="428" cy="744" r="9.5"/><text class="step-number" x="428" y="748">6</text>
      <circle class="step-dot" cx="492" cy="764" r="9.5"/><text class="step-number" x="492" y="768">7</text>
    </g>

    <g transform="translate(90,679)">
      <polygon class="icon-side" points="0,4 4,0 4,20 0,24"/>
      <rect class="icon-face" x="4" y="0" width="22" height="20"/>
      <path class="icon-solid" d="M9 11 L15 6 L21 11 L21 16 L9 16 Z"/>
    </g>
    <text class="step-label" x="102" y="730">Listening</text>

    <g transform="translate(154,657)">
      <polygon class="icon-side" points="0,4 4,0 4,20 0,24"/>
      <rect class="icon-face" x="4" y="0" width="22" height="20"/>
      <circle class="icon-glyph" cx="14" cy="9" r="4"/>
      <line class="icon-glyph" x1="17" y1="12" x2="21" y2="16"/>
    </g>
    <text class="step-label" x="166" y="708">Visioning</text>

    <g transform="translate(219,646)">
      <polygon class="icon-side" points="0,4 4,0 4,20 0,24"/>
      <rect class="icon-face" x="4" y="0" width="22" height="20"/>
      <path class="icon-glyph" d="M11 16 L12 12 L19 5 L21 7 L14 14 Z"/>
    </g>
    <text class="step-label" x="231" y="696">Planning</text>

    <g transform="translate(284,646)">
      <polygon class="icon-side" points="0,4 4,0 4,20 0,24"/>
      <rect class="icon-face" x="4" y="0" width="22" height="20"/>
      <circle class="icon-solid" cx="15" cy="9" r="3.5"/>
      <rect class="icon-solid" x="13.5" y="12.5" width="3" height="3"/>
      <path class="icon-glyph" d="M15 2.5 V3.5 M9 9 H8 M22 9 H21 M10.5 4.5 L11.2 5.2 M19.5 4.5 L18.8 5.2"/>
    </g>
    <text class="step-label" x="296" y="696">Designing</text>

    <g transform="translate(350,646)">
      <polygon class="icon-side" points="0,4 4,0 4,20 0,24"/>
      <rect class="icon-face" x="4" y="0" width="22" height="20"/>
      <circle class="icon-glyph" cx="15" cy="10" r="4.5" stroke-dasharray="2 1.5"/>
      <circle class="icon-glyph" cx="15" cy="10" r="1.8"/>
    </g>
    <text class="step-label" x="362" y="696">Managing</text>

    <g transform="translate(416,657)">
      <polygon class="icon-side" points="0,4 4,0 4,20 0,24"/>
      <rect class="icon-face" x="4" y="0" width="22" height="20"/>
      <path class="icon-solid" d="M10 6 L17 6 L19 8 L15 9 Z"/>
      <line class="icon-glyph" x1="14" y1="8" x2="20" y2="15" stroke-width="2"/>
    </g>
    <text class="step-label" x="428" y="708">Installing</text>

    <g transform="translate(480,679)">
      <polygon class="icon-side" points="0,4 4,0 4,20 0,24"/>
      <rect class="icon-face" x="4" y="0" width="22" height="20"/>
      <path class="icon-glyph" d="M9 10 L13 14 L21 5" stroke-width="2.2"/>
    </g>
    <text class="step-label" x="492" y="730">Completing</text>
  </svg>
</main>
</body>
</html>
```